Website for software company "velbra"

We need a website for our software company/startup named "velbra". We are developing several products (currently 3 standard-software products) which are all in different sectors, but all our products are available for Laptops/PC/Mobile Phones/Tablets, ... We do also create custom software and support our customers with consulting to optimize their processes.
We already have a Logo which you can find in the attached files.
We are a young team of 4 members (two founders and 2 employees).

To get an idea of our products -> the first one is a planning software for healthcare organizations (eg. Mercyway, firebrigade, pharmacy), the second one is a booking software for sport clubs and the third one is a competition software for sports hunting. You see very diverse. Include or ignore this info of our products as you like.

The design has to be a bootstrap 4 (or higher) design. We have licenced FontAwesome as iconset. Responsive design should come without saying.

Coding

Coded - Design and coding required

Number of Pages Required

5+ page

Font styles to use
Sans Serif

Requirements
Must have
• Starting page, product pages, news section, contact, team, services

```html
<!DOCTYPE html>
<html lang="en">
<head>
<meta charset="utf-8">
<title>velbra – Website and Banners</title>
<link href="https://fonts.googleapis.com/css2?family=Montserrat:wght@300;400;500;600;700;800&display=swap" rel="stylesheet">
<style>
:root{
  --dark:#262b35;
  --dark-2:#1e222b;
  --orange:#f47b20;
  --orange-2:#f6913b;
  --white:#ffffff;
  --board:#d5d5d5;
  --light:#eef0f4;
  --grey-text:#6b6f78;
  --text:#2a2e36;
  --purple:#6a5ae0;
  --teal:#3fb6a8;
  --blue:#3d8bd9;
}
*{box-sizing:border-box;margin:0;padding:0}
html,body{width:1200px;height:2212px;overflow:hidden}
body{background:var(--board);font-family:'Montserrat',sans-serif;color:var(--text)}
.board{position:relative;width:1200px;height:2212px;overflow:hidden;background:var(--board)}
.abs{position:absolute}

/* shared */
.logo{position:absolute;display:flex;align-items:center;gap:4px;font-weight:600;font-size:18px;letter-spacing:.5px;color:var(--white);line-height:1;z-index:2}
.logo .mark{width:9px;height:9px;background:var(--orange)}
.logo.dark{color:var(--text)}
.nav{position:absolute;display:flex;align-items:center;justify-content:space-between;font-size:5px;font-weight:600;color:var(--white);letter-spacing:.2px;z-index:2}
.nav.dark{color:#555a63}
.nav .on{color:var(--orange);border-bottom:1px solid var(--orange);padding-bottom:2px}
.nav .cta{border:1px solid currentColor;border-radius:9px;padding:3px 11px}
.nav .cta.square{border-radius:0;border-color:#fff;padding:3px 12px}
.nav .cta.fill{background:var(--dark);color:#fff;border-color:var(--dark);border-radius:0}
.btn{position:absolute;display:flex;align-items:center;justify-content:center;height:17px;border-radius:9px;background:var(--orange);color:#fff;font-size:5px;font-weight:700;letter-spacing:.3px}
.btn.sq{border-radius:0}
.btn.dark{background:var(--dark)}
.btn.outline{background:transparent;border:1px solid var(--orange);color:var(--orange)}
.headline{position:absolute;font-size:14px;line-height:1.15;color:var(--white);font-weight:700;text-transform:uppercase}
.headline .light{font-weight:300}
.headline.dark{color:var(--text)}
.lead{position:absolute;font-size:5.6px;line-height:1.55;color:#c9ccd2}
.lead.dark{color:var(--grey-text)}
.kicker{position:absolute;font-size:6px;font-weight:600;color:var(--orange)}
.sec-title{position:absolute;font-size:14px;font-weight:300;color:var(--text);text-transform:uppercase;letter-spacing:.3px}
.sec-title b{font-weight:700}
.body{position:absolute;font-size:5.4px;line-height:1.75;color:var(--grey-text)}
.photo{position:absolute}

/* dashboard mockups */
.dash{position:absolute;background:#fff;border-radius:2px;box-shadow:0 3px 10px rgba(0,0,0,.22);overflow:hidden}
.dash .top{position:absolute;left:0;top:0;right:0;height:5px;background:var(--orange)}
.dash .ttl{position:absolute;left:5%;top:9px;font-size:5px;font-weight:500;color:#333}
.dash .bars{position:absolute;left:5%;top:24%;width:55%;height:30%;display:flex;align-items:flex-end;gap:5%;border-bottom:1px solid #e3e5ea}
.dash .bars span{flex:1;height:45%;background:var(--purple)}
.dash .bars span:nth-child(2n){background:var(--teal);height:70%}
.dash .bars span:nth-child(3n){background:var(--blue);height:90%}
.dash .bars span:nth-child(4n){height:55%}
.dash .bars span:nth-child(5n){height:100%}
.dash .map{position:absolute;left:5%;top:60%;width:55%;height:32%;background:linear-gradient(135deg,#e4e7ee,#d5d9e2);border-radius:2px}
.dash .side{position:absolute;left:66%;top:24%;width:29%;height:68%;display:flex;flex-direction:column;justify-content:space-between}
.dash .side i{display:block;height:3px;border-radius:2px;background:#e1e4ea}
.dash .side i:nth-child(2n){background:var(--purple);width:70%}
.dash .side i:nth-child(3n){background:var(--teal);width:45%}
.dash .stats{position:absolute;left:66%;top:11%;width:29%;display:flex;justify-content:space-between}
.dash .stats b{width:6px;height:6px;border-radius:50%;background:var(--purple)}
.dash.wave .line{position:absolute;left:6%;top:22%;width:88%;height:40%}
.dash.plain .top{display:none}
.dash .strip{position:absolute;left:5%;bottom:8%;width:90%;height:14%;display:flex;gap:4%}
.dash .strip span{flex:1;background:#edf0f5;border-radius:2px}

.phone{position:absolute;background:#fff;border-radius:7px;box-shadow:0 3px 10px rgba(0,0,0,.25);overflow:hidden;border:2px solid #f1f2f5}
.phone .head{height:32%;background:linear-gradient(180deg,#3c8ed4,#5aa7e0)}
.phone .head.light{height:18%;background:#f4f5f8}
.phone .row{display:flex;justify-content:space-between;align-items:center;margin:6% 8% 0}
.phone .row i{display:block;height:3px;width:45%;background:#d9dce3;border-radius:2px}
.phone .row b{display:block;width:14px;height:6px;background:#7cc57a;border-radius:2px}
.phone .row b.o{background:var(--orange);width:6px;height:6px;border-radius:50%}

.panel-grey{position:absolute;background:#e9ebef}

/* ===== website column ===== */
.site{position:absolute;left:85px;top:70px;width:482px;height:2041px;background:#fff;overflow:hidden}
.hero{position:absolute;left:0;top:0;width:482px;height:290px;background:radial-gradient(circle at 30% 40%,#353b47,var(--dark) 60%)}
.hero .edge{position:absolute;left:0;top:228px}
.about-feature{position:absolute;left:252px;width:200px}
.about-feature .ico{position:absolute;left:0;top:0;width:26px;height:26px;border-radius:50%;background:var(--dark);display:flex;align-items:center;justify-content:center}
.about-feature .ico.grey{background:#eceef2}
.about-feature .ico.orange{background:var(--orange)}
.about-feature h4{position:absolute;left:32px;top:2px;font-size:5.6px;font-weight:700;color:var(--text)}
.about-feature p{position:absolute;left:32px;top:10px;width:170px;font-size:5px;line-height:1.7;color:var(--grey-text)}

.split{position:absolute;left:0;top:577px;width:482px;height:182px}
.split .services{position:absolute;left:0;top:0;width:239px;height:182px;background:linear-gradient(135deg,var(--orange-2),var(--orange))}
.split .team{position:absolute;left:239px;top:0;width:243px;height:182px;background:linear-gradient(135deg,#2f3541,#1f232b)}
.split .sec-title{color:#fff;width:100%;text-align:center;top:46px;font-size:13px}
.split .body{color:rgba(255,255,255,.85);width:180px;text-align:center;top:71px}

.product h3{position:absolute;font-size:11px;font-weight:700;color:var(--text);border-left:2px solid var(--orange);padding-left:6px;line-height:1}
.news{position:absolute;left:0;top:1443px;width:482px;height:252px;background:#f1f2f4}
.news-card{position:absolute;background:#fff;border:1px solid #e1e3e8}
.news-card .pic{position:absolute;left:0;top:0;width:50%;height:100%}
.news-card .date{position:absolute;left:55%;top:12px;background:var(--orange);color:#fff;font-size:3.6px;font-weight:700;padding:2px 4px}
.news-card h5{position:absolute;left:55%;top:25px;font-size:4.6px;font-weight:700;color:var(--text)}
.news-card p{position:absolute;left:55%;top:33px;width:40%;font-size:4.2px;line-height:1.6;color:var(--grey-text)}
.contact{position:absolute;left:0;top:1695px;width:482px;height:205px;background:linear-gradient(180deg,var(--orange-2),var(--orange))}
.field{position:absolute;left:58px;width:146px;height:16px;background:#fff;font-size:4.6px;color:#666;padding:5px 7px}
.footer{position:absolute;left:0;top:1900px;width:482px;height:141px;background:var(--dark);color:#fff}
.footer .col{position:absolute;top:31px;border-left:1.5px solid var(--orange);padding-left:9px;height:60px}
.footer .col h6{font-size:5px;font-weight:700;margin-bottom:7px}
.footer .col li{list-style:none;font-size:4.6px;color:#c7cad0;margin-bottom:6px}
.social{display:flex;gap:3px}
.social span{width:11px;height:11px;border-radius:50%;border:1px solid #fff}
.social span:first-child{background:var(--orange);border-color:var(--orange)}

/* ===== banner column ===== */
.banners{position:absolute;left:617px;top:66px;width:487px;height:1994px;background:#fff;overflow:hidden}
.banners .title{position:absolute;left:0;top:10px;width:100%;text-align:center;font-size:33px;font-weight:800;color:#111;letter-spacing:.5px}
.banner{position:absolute;left:0;width:487px;overflow:hidden}
.banner.dark{background:radial-gradient(circle at 40% 30%,#333946,var(--dark) 65%)}
.banner.light{background:var(--light)}
.banner svg{position:absolute;left:0}
</style>
</head>
<body>
<div class="board">

  <!-- ================= WEBSITE ================= -->
  <main class="site">

    <!-- hero -->
    <section class="hero">
      <svg class="edge" width="482" height="62" viewBox="0 0 482 62">
        <polygon points="0,2 158,47 482,-3 482,7 158,58 0,9" fill="var(--orange)"/>
        <polygon points="0,9 158,58 482,7 482,62 0,62" fill="#fff"/>
      </svg>
      <div class="logo" style="left:51px;top:20px"><span class="mark"></span>VELBRA</div>
      <nav class="nav" style="left:170px;top:19px;width:267px">
        <span class="on">PRODUCT</span><span>SERVICES</span><span>NEWS</span><span>TEAM</span><span>ABOUT</span><span class="cta">CONTACT</span>
      </nav>
      <h1 class="headline" style="left:47px;top:92px;font-size:13.5px"><span class="light">We help customer</span><br>to optimize their<br>processes</h1>
      <p class="lead" style="left:48px;top:147px;width:165px">Lorem ipsum dolor sit amet, consectetur adipiscing elit, sed do eiusmod tempor incididunt.</p>
      <div class="btn" style="left:47px;top:171px;width:67px">LEARN MORE</div>

      <div class="dash" style="left:240px;top:64px;width:176px;height:135px">
        <div class="top"></div><div class="ttl">Overview</div>
        <div class="stats"><b></b><b></b><b></b></div>
        <div class="bars"><span></span><span></span><span></span><span></span><span></span><span></span><span></span><span></span><span></span><span></span></div>
        <div class="map" role="img" aria-label="World map of active customers"></div>
        <div class="side"><i></i><i></i><i></i><i></i><i></i><i></i></div>
      </div>
      <div class="dash wave plain" style="left:334px;top:140px;width:105px;height:71px">
        <svg class="line" viewBox="0 0 100 40" preserveAspectRatio="none"><path d="M0,30 C10,10 18,35 28,18 S45,30 55,15 72,30 82,12 95,25 100,20 L100,40 L0,40Z" fill="#dce9f8"/><path d="M0,30 C10,10 18,35 28,18 S45,30 55,15 72,30 82,12 95,25 100,20" fill="none" stroke="#4a90e2" stroke-width="1.5"/></svg>
        <div class="strip"><span></span><span></span><span></span></div>
      </div>
    </section>

    <!-- about -->
    <section>
      <h2 class="sec-title" style="left:0;top:306px;width:482px;text-align:center">About <b>Velbra</b></h2>
      <p class="body" style="left:105px;top:329px;width:272px;text-align:center">Lorem ipsum dolor sit amet, consectetur adipiscing elit, sed do eiusmod tempor incididunt ut laborLorem ipsum dolor sit amet, consectetur adipiscing elit, sed do eiusmo</p>
      <div class="photo" role="img" aria-label="Team member working on a laptop, framed by angled shapes" style="left:72px;top:368px;width:143px;height:167px;background:linear-gradient(135deg,#b9c4d0,#6e7f93 55%,#d9a27a);clip-path:polygon(0 0,68% 48%,68% 0,100% 0,100% 100%,68% 100%,68% 52%,0 100%)"></div>

      <div class="about-feature" style="top:378px">
        <div class="ico"><svg width="14" height="14" viewBox="0 0 14 14"><circle cx="7" cy="7" r="5" fill="none" stroke="#fff" stroke-width="1"/><circle cx="7" cy="7" r="2" fill="none" stroke="#fff" stroke-width="1"/></svg></div>
        <h4>OPTIMIZE</h4>
        <p>Lorem ipsum dolor sit amet, consectetur adipiscing elit, sed do eiusmod tempor incididunt ut.</p>
      </div>
      <div class="about-feature" style="top:424px">
        <div class="ico grey"><svg width="14" height="12" viewBox="0 0 14 12"><rect x="1" y="1" width="12" height="10" fill="none" stroke="var(--orange)" stroke-width="1"/><path d="M5,4 L3,6 L5,8 M9,4 L11,6 L9,8" fill="none" stroke="var(--orange)" stroke-width="1"/></svg></div>
        <h4>DEVELOP</h4>
        <p>Lorem ipsum dolor sit amet, consectetur adipiscing elit, sed do eiusmod tempor incididunt ut.</p>
      </div>
      <div class="about-feature" style="top:470px">
        <div class="ico orange"><svg width="14" height="14" viewBox="0 0 14 14"><circle cx="7" cy="6" r="3" fill="none" stroke="#fff" stroke-width="1.2"/><path d="M2,12 C4,9 10,9 12,12" fill="none" stroke="#fff" stroke-width="1.2"/></svg></div>
        <h4>SUPPORT</h4>
        <p>Lorem ipsum dolor sit amet, consectetur adipiscing elit, sed do eiusmod tempor incididunt ut.</p>
      </div>
      <div class="btn outline" style="left:252px;top:513px;width:68px;height:19px">LEARN MORE</div>
    </section>

    <!-- services / team -->
    <section class="split">
      <div class="services">
        <h2 class="sec-title">Our <b>Services</b></h2>
        <p class="body" style="left:30px">Lorem ipsum dolor sit amet, consectetur adipiscing elit, sed do eiusmod tempor incididunt ut laborLorem ipsum dolor sit amet, consectetur adipiscing elit, sed do eiusmo</p>
        <div class="btn dark" style="left:103px;top:133px;width:67px">LEARN MORE</div>
      </div>
      <div class="team">
        <h2 class="sec-title">Meet <b>Our Team</b></h2>
        <p class="body" style="left:32px">Lorem ipsum dolor sit amet, consectetur adipiscing elit, sed do eiusmod tempor incididunt ut laborLorem ipsum dolor sit amet, consectetur adipiscing elit, sed do eiusmo</p>
        <div class="btn" style="left:88px;top:130px;width:67px">LEARN MORE</div>
      </div>
    </section>

    <!-- products -->
    <section>
      <h2 class="sec-title" style="left:0;top:783px;width:482px;text-align:center">Our <b>Products</b></h2>
      <div class="abs" style="left:234px;top:803px;width:14px;height:1.5px;background:var(--orange)"></div>

      <div class="product">
        <h3 style="left:52px;top:854px">PLANNING SOFTWARE</h3>
        <p class="body" style="left:58px;top:872px;width:175px">Lorem ipsum dolor sit amet, consectetur adipiscing elit, sed do eiusmod tempor incididunt ut labore et dolore magna aliqua. Ut enim ad minim veniam, quis nostrud<br><br>exercitation ullamco laboris nisi ut aliquip ex ea commodo consequat. Duis aute irure dolo</p>
        <div class="btn" style="left:57px;top:942px;width:67px">LEARN MORE</div>
        <div class="panel-grey" style="left:390px;top:838px;width:92px;height:142px"></div>
        <div class="dash wave plain" style="left:254px;top:840px;width:170px;height:108px;border:3px solid #2b2f36;border-radius:4px">
          <svg class="line" style="top:14%;width:45%;height:22%" viewBox="0 0 100 40" preserveAspectRatio="none"><path d="M0,32 C20,28 30,30 45,24 S70,5 80,20 95,28 100,26 L100,40 L0,40Z" fill="#cfe3f7"/></svg>
          <div class="abs" style="left:60%;top:16%;font-size:7px;color:#4a90e2">$ 15.000</div>
          <div class="abs" style="left:6%;top:42%;width:26%;height:20%;display:flex;align-items:flex-end;gap:2px"><span style="flex:1;height:40%;background:#9fc5ee"></span><span style="flex:1;height:80%;background:#9fc5ee"></span><span style="flex:1;height:55%;background:#9fc5ee"></span><span style="flex:1;height:95%;background:#4a90e2"></span><span style="flex:1;height:60%;background:#9fc5ee"></span></div>
          <svg class="abs" style="left:38%;top:42%" width="44" height="18" viewBox="0 0 44 18"><circle cx="8" cy="9" r="6" fill="none" stroke="#4a90e2" stroke-width="2"/><circle cx="22" cy="9" r="6" fill="none" stroke="#4a90e2" stroke-width="2"/><circle cx="36" cy="9" r="6" fill="none" stroke="#4a90e2" stroke-width="2"/></svg>
          <div class="strip" style="height:26%"><span></span><span></span></div>
        </div>
        <div class="abs" style="left:232px;top:948px;width:212px;height:5px;background:linear-gradient(#e6e7ea,#b9bcc2);border-radius:0 0 6px 6px"></div>
      </div>

      <div class="product">
        <div class="abs" style="left:35px;top:1020px;width:142px;height:157px;background:linear-gradient(135deg,var(--orange-2),var(--orange))"></div>
        <div class="dash plain" style="left:48px;top:1035px;width:176px;height:129px">
          <div class="ttl" style="top:5px">Overview</div>
          <div class="stats"><b></b><b></b><b></b></div>
          <div class="bars"><span></span><span></span><span></span><span></span><span></span><span></span><span></span><span></span><span></span><span></span></div>
          <div class="map" role="img" aria-label="World map of bookings"></div>
          <div class="side"><i></i><i></i><i></i><i></i><i></i><i></i></div>
        </div>
        <h3 style="left:262px;top:1052px">BOOKING SOFTWARE</h3>
        <p class="body" style="left:267px;top:1070px;width:175px">Lorem ipsum dolor sit amet, consectetur adipiscing elit, sed do eiusmod tempor incididunt ut labore et dolore magna aliqua. Ut enim ad minim veniam, quis nostrud<br><br>exercitation ullamco laboris nisi ut aliquip ex ea commodo consequat. Duis aute irure dolo</p>
        <div class="btn" style="left:266px;top:1140px;width:67px">LEARN MORE</div>
      </div>

      <div class="product">
        <h3 style="left:51px;top:1262px">COMPETITION SOFTWARE</h3>
        <p class="body" style="left:56px;top:1280px;width:175px">Lorem ipsum dolor sit amet, consectetur adipiscing elit, sed do eiusmod tempor incididunt ut labore et dolore magna aliqua. Ut enim ad minim veniam, quis nostrud<br><br>exercitation ullamco laboris nisi ut aliquip ex ea commodo consequat. Duis aute irure dolo</p>
        <div class="btn" style="left:55px;top:1350px;width:67px">LEARN MORE</div>
        <div class="panel-grey" style="left:284px;top:1220px;width:163px;height:141px"></div>
        <div class="dash wave plain" style="left:241px;top:1241px;width:189px;height:145px;border:4px solid #15181d;border-radius:6px">
          <svg class="line" style="top:10%;width:55%;height:40%" viewBox="0 0 100 40" preserveAspectRatio="none"><path d="M0,30 L25,10 L45,25 L70,8 L100,20" fill="none" stroke="#4a90e2" stroke-width="1" stroke-dasharray="3 2"/></svg>
          <div class="abs" style="left:6%;top:80%;font-size:6px;color:var(--orange);display:flex;gap:8px"><span>$7.500</span><span>$1.100</span><span>$1.200</span></div>
        </div>
        <div class="phone" style="left:339px;top:1271px;width:60px;height:124px"><div class="head"></div><div class="row"><i></i><b></b></div><div class="row"><i></i><b></b></div><div class="row"><i></i><b></b></div><div class="row"><i></i><b></b></div></div>
      </div>
    </section>

    <!-- news -->
    <section class="news">
      <h2 class="sec-title" style="left:61px;top:30px;font-size:13px">Latest <b>News</b></h2>
      <div class="abs" style="left:61px;top:48px;width:14px;height:1.5px;background:var(--orange)"></div>
      <div class="photo" role="img" aria-label="Developer workstation with monitors" style="left:61px;top:61px;width:188px;height:148px;background:linear-gradient(160deg,#5b4a3a,#2e3a36 45%,#1c2226)">
        <span class="abs" style="left:20px;top:107px;background:var(--orange);color:#fff;font-size:3.8px;font-weight:700;padding:2px 5px">28 MAY 2021</span>
        <p class="abs" style="left:14px;top:118px;width:165px;font-size:6px;font-weight:700;color:#fff;line-height:1.3">Lorem ipsum dolor sit amet, consectetur adipiscing elit, sed do eiusmod tempor</p>
      </div>
      <article class="news-card" style="left:253px;top:61px;width:174px;height:71px">
        <div class="pic" role="img" aria-label="Hands typing on a laptop" style="background:linear-gradient(135deg,#8a9aa8,#3b4650)"></div>
        <span class="date">19 MAY 2021</span><h5>Lorem ipsum dolor sit</h5>
        <p>Duis aute irure dolor in reprehenderit in voluptate velit esse cillum dolore eu fugiat</p>
      </article>
      <article class="news-card" style="left:253px;top:139px;width:174px;height:70px">
        <div class="pic" role="img" aria-label="Programmers at screens in a dark office" style="background:linear-gradient(135deg,#2b5b86,#162838)"></div>
        <span class="date">18 MAY 2021</span><h5>Lorem ipsum dolor sit</h5>
        <p>Duis aute irure dolor in reprehenderit in voluptate velit esse cillum dolore eu fugiat</p>
      </article>
    </section>

    <!-- contact -->
    <section class="contact">
      <div class="photo" role="img" aria-label="Two developers working together in front of code screens" style="left:228px;top:0;width:254px;height:205px;background:linear-gradient(120deg,#3a2b22,#8a5a34 45%,#2a3340);clip-path:polygon(36% 0,100% 0,100% 100%,36% 100%,0 50%)"></div>
      <h2 class="sec-title" style="left:58px;top:36px;color:#fff;font-size:13px">Contact <b>Velbra</b></h2>
      <div class="field" style="top:62px">Name*</div>
      <div class="field" style="top:82px">Email address*</div>
      <div class="field" style="top:101px">Phone*</div>
      <div class="field" style="top:120px;height:31px">Message</div>
      <div class="btn dark" style="left:56px;top:165px;width:60px;height:15px">CONTACT US</div>
    </section>

    <!-- footer -->
    <footer class="footer">
      <div class="logo" style="left:61px;top:28px"><span class="mark"></span>VELBRA</div>
      <p class="abs" style="left:61px;top:52px;width:95px;font-size:4.3px;line-height:1.6;color:#c7cad0">Lorem ipsum dolor sit amet, consectetur adipiscing elit, sed do eiusmod tempor incididunt ut labore et dolore</p>
      <div class="col" style="left:180px"><h6>NAVIGATION</h6><ul><li>About Us</li><li>Products</li><li>Services</li><li>Contact Us</li></ul></div>
      <div class="col" style="left:275px"><h6>RESOURCES</h6><ul><li>News</li><li>Team</li><li>Privacy Policy</li></ul></div>
      <div class="col" style="left:364px"><h6>FOLLOW US</h6><div class="social"><span></span><span></span><span></span><span></span></div></div>
      <p class="abs" style="left:0;top:124px;width:482px;text-align:center;font-size:4.3px;color:#c7cad0">© 2022 Velbra | All Rights Reserved</p>
    </footer>
  </main>

  <!-- ================= BANNERS ================= -->
  <aside class="banners">
    <h2 class="title">BANNERS</h2>

    <!-- banner 1 -->
    <section class="banner dark" style="top:75px;height:364px">
      <svg style="top:0" width="487" height="364" viewBox="0 0 487 364"><path d="M0,205 C110,275 260,300 487,285 L487,364 L0,364Z" fill="#fff"/></svg>
      <div class="logo" style="left:51px;top:23px"><span class="mark"></span>VELBRA</div>
      <nav class="nav" style="left:171px;top:24px;width:270px"><span class="on">PRODUCT</span><span>SERVICES</span><span>NEWS</span><span>TEAM</span><span>ABOUT</span><span class="cta">CONTACT</span></nav>
      <h1 class="headline" style="left:0;top:71px;width:487px;text-align:center"><span class="light">We help customer to</span><br>optimize their processes</h1>
      <p class="lead" style="left:150px;top:106px;width:187px;text-align:center">Lorem ipsum dolor sit amet, consectetur adipiscing elit, sed do eiusmod tempor incididunt.</p>
      <div class="btn" style="left:212px;top:131px;width:62px;height:16px">LEARN MORE</div>
      <div class="dash plain" style="left:96px;top:185px;width:62px;height:111px"><div class="top" style="display:block;background:#2b2f36;height:6px"></div><div class="side" style="left:8%;width:84%;top:12%"><i></i><i></i><i></i><i></i><i></i><i></i></div></div>
      <div class="dash plain" style="left:330px;top:185px;width:58px;height:111px"><div class="top" style="display:block;background:#2b2f36;height:6px"></div><div class="bars" style="left:10%;width:80%;top:40%;height:20%"><span></span><span></span><span></span><span></span><span></span></div></div>
      <div class="dash" style="left:157px;top:165px;width:176px;height:135px">
        <div class="top"></div><div class="ttl">Overview</div><div class="stats"><b></b><b></b><b></b></div>
        <div class="bars"><span></span><span></span><span></span><span></span><span></span><span></span><span></span><span></span><span></span><span></span></div>
        <div class="map" role="img" aria-label="World map of active customers"></div>
        <div class="side"><i></i><i></i><i></i><i></i><i></i><i></i></div>
      </div>
    </section>

    <!-- banner 2 -->
    <section class="banner" style="top:439px;height:316px;background:#fff">
      <div class="abs" style="left:0;top:0;width:487px;height:280px;background:radial-gradient(circle at 30% 60%,#30363f,#1d2129 70%)"></div>
      <svg style="top:0" width="487" height="316" viewBox="0 0 487 316">
        <path d="M0,262 C160,255 330,235 487,205 L487,240 C330,252 150,265 0,272Z" fill="var(--orange)"/>
        <path d="M0,272 C150,265 330,252 487,240 L487,316 L0,316Z" fill="#fff"/>
      </svg>
      <div class="logo" style="left:49px;top:17px"><span class="mark"></span>VELBRA</div>
      <nav class="nav" style="left:168px;top:20px;width:270px"><span class="on">PRODUCT</span><span>SERVICES</span><span>NEWS</span><span>TEAM</span><span>ABOUT</span><span class="cta square">CONTACT</span></nav>
      <h1 class="headline" style="left:48px;top:91px"><span class="light">We help customer to</span><br>to optimize their<br>processes</h1>
      <p class="lead" style="left:48px;top:140px;width:160px">Lorem ipsum dolor sit amet, consectetur adipiscing elit, sed do eiusmod tempor incididunt.</p>
      <div class="btn sq" style="left:48px;top:163px;width:62px;height:15px">LEARN MORE</div>
      <div class="dash plain" style="left:297px;top:69px;width:133px;height:137px">
        <div class="stats"><b></b><b></b><b></b></div>
        <div class="bars"><span></span><span></span><span></span><span></span><span></span><span></span><span></span><span></span></div>
        <div class="map" role="img" aria-label="World map of bookings"></div>
        <div class="side"><i></i><i></i><i></i><i></i></div>
      </div>
      <div class="dash plain" style="left:360px;top:138px;width:85px;height:60px;background:#eef2fa"><div class="side" style="left:6%;width:50%;top:15%"><i></i><i></i><i></i><i></i><i></i></div><svg class="abs" style="left:62%;top:25%" width="26" height="16" viewBox="0 0 26 16"><path d="M3,14 A10,10 0 0 1 23,14" fill="none" stroke="#4a90e2" stroke-width="2"/></svg></div>
      <div class="phone" style="left:227px;top:65px;width:69px;height:143px"><div class="head"></div><div class="row"><i></i><b></b></div><div class="row"><i></i><b></b></div><div class="row"><i></i><b></b></div><div class="row"><i></i><b></b></div></div>
    </section>

    <!-- banner 3 -->
    <section class="banner light" style="top:755px;height:261px">
      <div class="abs" style="left:244px;top:-37px;width:300px;height:300px;border-radius:50%;background:var(--orange)"></div>
      <div class="logo dark" style="left:49px;top:13px"><span class="mark"></span>VELBRA</div>
      <nav class="nav dark" style="left:164px;top:18px;width:272px"><span class="on">PRODUCT</span><span>SERVICES</span><span style="color:#fff">NEWS</span><span style="color:#fff">TEAM</span><span style="color:#fff">ABOUT</span><span class="cta fill">CONTACT</span></nav>
      <p class="kicker" style="left:53px;top:85px">WELCOME TO VELBRA</p>
      <h1 class="headline dark" style="left:53px;top:97px"><span class="light">We help customer to</span><br>to optimize their<br>processes</h1>
      <p class="lead dark" style="left:53px;top:148px;width:170px">Lorem ipsum dolor sit amet, consectetur adipiscing elit, sed do eiusmod tempor incididunt.</p>
      <div class="btn sq" style="left:53px;top:177px;width:66px">LEARN MORE</div>
      <div class="dash wave plain" style="left:296px;top:51px;width:200px;height:152px;background:#f6f7fb">
        <div class="ttl" style="font-weight:700;color:var(--blue)">Hi Lena Marsh!</div>
        <svg class="line" style="left:22%;top:22%;width:60%;height:30%" viewBox="0 0 100 40" preserveAspectRatio="none"><path d="M0,30 L15,12 L30,22 L45,18 L60,28 L78,12 L100,8" fill="none" stroke="var(--orange)" stroke-width="1.5"/></svg>
        <div class="side" style="left:22%;top:60%;width:55%;height:32%"><i></i><i></i><i></i><i></i></div>
      </div>
      <div class="phone" style="left:264px;top:85px;width:67px;height:135px"><div class="head light"></div><div class="row"><i></i><b class="o"></b></div><div class="row"><i></i><b class="o"></b></div><div class="row"><i></i><b class="o"></b></div><div class="row"><i></i><b class="o"></b></div></div>
    </section>

    <!-- banner 4 -->
    <section class="banner light" style="top:1053px;height:261px">
      <svg style="top:0" width="487" height="261" viewBox="0 0 487 261"><polygon points="250,48 292,88 250,88" fill="var(--orange)"/><polygon points="250,120 262,112 262,200 250,208" fill="var(--dark)"/></svg>
      <div class="logo dark" style="left:51px;top:13px"><span class="mark"></span>VELBRA</div>
      <nav class="nav dark" style="left:166px;top:18px;width:272px"><span class="on">PRODUCT</span><span>SERVICES</span><span>NEWS</span><span>TEAM</span><span>ABOUT</span><span class="cta fill">CONTACT</span></nav>
      <p class="kicker" style="left:56px;top:85px">WELCOME TO VELBRA</p>
      <h1 class="headline dark" style="left:56px;top:97px"><span class="light">We help customer to</span><br>to optimize their<br>processes</h1>
      <p class="lead dark" style="left:56px;top:148px;width:170px">Lorem ipsum dolor sit amet, consectetur adipiscing elit, sed do eiusmod tempor incididunt.</p>
      <div class="btn sq" style="left:56px;top:177px;width:66px">LEARN MORE</div>
      <div class="dash wave plain" style="left:297px;top:51px;width:200px;height:152px;background:#f6f7fb">
        <div class="ttl" style="font-weight:700;color:var(--blue)">Hi Lena Marsh!</div>
        <svg class="line" style="left:22%;top:22%;width:60%;height:30%" viewBox="0 0 100 40" preserveAspectRatio="none"><path d="M0,30 L15,12 L30,22 L45,18 L60,28 L78,12 L100,8" fill="none" stroke="var(--orange)" stroke-width="1.5"/></svg>
        <div class="side" style="left:22%;top:60%;width:55%;height:32%"><i></i><i></i><i></i><i></i></div>
      </div>
      <div class="phone" style="left:265px;top:85px;width:67px;height:135px"><div class="head light"></div><div class="row"><i></i><b class="o"></b></div><div class="row"><i></i><b class="o"></b></div><div class="row"><i></i><b class="o"></b></div><div class="row"><i></i><b class="o"></b></div></div>
    </section>

    <!-- banner 5 -->
    <section class="banner" style="top:1348px;height:317px;background:#fff">
      <div class="abs" style="left:0;top:0;width:487px;height:290px;background:linear-gradient(100deg,#1e232c 40%,#3a3330 75%,#6a4a2c)"></div>
      <div class="photo" role="img" aria-label="Hands typing on a laptop showing an analytics dashboard" style="left:250px;top:40px;width:237px;height:200px;background:radial-gradient(ellipse at 60% 50%,#9aa4b2,#4b5360 45%,transparent 75%)"></div>
      <svg style="top:0" width="487" height="317" viewBox="0 0 487 317">
        <polygon points="0,228 244,268 487,222 487,234 244,284 0,240" fill="var(--orange)"/>
        <polygon points="0,240 244,284 487,234 487,317 0,317" fill="#fff"/>
      </svg>
      <div class="logo" style="left:58px;top:13px"><span class="mark"></span>VELBRA</div>
      <nav class="nav" style="left:170px;top:20px;width:270px"><span class="on" style="color:#fff;border-color:#fff">PRODUCT</span><span>SERVICES</span><span>NEWS</span><span>TEAM</span><span>ABOUT</span><span class="cta square" style="border-color:var(--orange)">CONTACT</span></nav>
      <p class="kicker" style="left:59px;top:85px">WELCOME TO VELBRA</p>
      <h1 class="headline" style="left:59px;top:97px"><span class="light">We help customer to</span><br>to optimize their<br>processes</h1>
      <p class="lead" style="left:59px;top:148px;width:170px">Lorem ipsum dolor sit amet, consectetur adipiscing elit, sed do eiusmod tempor incididunt.</p>
      <div class="btn sq" style="left:59px;top:170px;width:66px">LEARN MORE</div>
    </section>

    <!-- banner 6 -->
    <section class="banner" style="top:1665px;height:328px;background:linear-gradient(100deg,#1f232b 35%,#3b3230 65%,#b45e22)">
      <svg style="top:0" width="487" height="328" viewBox="0 0 487 328">
        <path d="M0,200 Q244,330 487,188 L487,328 L0,328Z" fill="var(--orange)"/>
        <path d="M0,210 Q244,340 487,198 L487,328 L0,328Z" fill="#fff"/>
      </svg>
      <div class="logo" style="left:44px;top:14px"><span class="mark"></span>VELBRA</div>
      <nav class="nav" style="left:164px;top:20px;width:273px"><span class="on">PRODUCT</span><span>SERVICES</span><span>NEWS</span><span>TEAM</span><span>ABOUT</span><span class="cta square">CONTACT</span></nav>
      <h1 class="headline" style="left:43px;top:92px"><span class="light">We help customer to</span><br>to optimize their<br>processes</h1>
      <p class="lead" style="left:43px;top:143px;width:160px">Lorem ipsum dolor sit amet, consectetur adipiscing elit, sed do eiusmod tempor incididunt.</p>
      <div class="btn sq" style="left:43px;top:166px;width:62px;height:15px">LEARN MORE</div>
      <div class="dash plain" style="left:291px;top:70px;width:133px;height:135px">
        <div class="stats"><b></b><b></b><b></b></div>
        <div class="bars"><span></span><span></span><span></span><span></span><span></span><span></span><span></span><span></span></div>
        <div class="map" role="img" aria-label="World map of bookings"></div>
        <div class="side"><i></i><i></i><i></i><i></i></div>
      </div>
      <div class="dash plain" style="left:355px;top:137px;width:85px;height:60px;background:#eef2fa"><div class="side" style="left:6%;width:50%;top:15%"><i></i><i></i><i></i><i></i><i></i></div><svg class="abs" style="left:62%;top:25%" width="26" height="16" viewBox="0 0 26 16"><path d="M3,14 A10,10 0 0 1 23,14" fill="none" stroke="#4a90e2" stroke-width="2"/></svg></div>
      <div class="phone" style="left:221px;top:66px;width:70px;height:144px"><div class="head"></div><div class="row"><i></i><b></b></div><div class="row"><i></i><b></b></div><div class="row"><i></i><b></b></div><div class="row"><i></i><b></b></div></div>
    </section>
  </aside>

</div>
</body>
</html>
```